Flyer Design for Business: "Velvet Glow"

My Business name is "VELVET GLOW"

Laser Hair Removal
Non invasive and pain free
Look amazing and feel confident with a Hair Free body
Now is the time to start don't delay
1 treatment a month will ensure you are bikini hot for the summer months
Take full advantage of our OPENING SPECIALS of 30%-40% savings
Part payments available

CELLULITE & FAT REDUCTION
Now you too can look amazing without invasive surgery, downtime or discomfort
Tara Wellbrook & Monica Farrowdale are avid recipients of this treatment.
Effective on all skin types and delivers fast measurable results for:
Helping mums regain their pre-baby figures
Losing the love handles (but keeping the love)
Stretch mark reduction
Skin tightening
Cellulite busting on Arms, tummy, thighs.
Man boob reduction.
Latest technology:
Bi Polar radio frequency (RF)
infrared light
negative pressure (Vacuum)
Tissue manipulation through roller mechanical massage.
50% saving Call now

PDT LED REJUVENATION LIGHT THERAPY
ORVA Researchers found:
Fibroblast and muscles grew 5 times faster, stimulates
reconstruction of collagenous fibres of the dermis
These findings and more assist with:
Remove freckles, sunburn pigmentation,
Cures acne and hair follicle inflammation
Anti aging skin tightening
Reduces pore size
Improve the skin texture
Improves circulation
Red light : reduces pore size, softens skin wrinkles,reduces acne
Blue light: Kills the acne bacillus to eliminate acne, inhibit inflammation
Yellow light: Skin tightening, whitening and softens skin wrinkles
Purple light: combination of red & blue lights treats acne scars
Orange light increases cell energy and accelerates metabolism
$55 Saving and relax under the lights.

Who can resist a soothing Hot stone massage therapy after:
A hard stressful day at work
Aches and muscular pain

Pick anything from this info with a couple of nice images.

Target Market(s)

Females & males Sports minded people cyclists

Industry/Entity Type

Beauty Salon

Colors
00a990
e34197

Requirements
Must have
• a couple of images and
Nice to have
• Pink and bluey green like my business card

```html
<!DOCTYPE html>
<html lang="en">
<head>
<meta charset="utf-8">
<title>Velvet Glow – Flyer</title>
<link rel="stylesheet" href="https://fonts.googleapis.com/css2?family=Lato:wght@300;400;700&display=swap">
<style>
  :root {
    --pink: #e34197;
    --teal: #00a990;
    --white: #ffffff;
    --paper: #ffffff;
    --stage: #e9e9eb;
    --grey: #d9d9db;
    --photo-skin: #d9c3b4;
    --photo-cool: #c9ccd3;
    --photo-red: #b94a4a;
  }
  * { box-sizing: border-box; margin: 0; padding: 0; }
  html, body { width: 1200px; height: 800px; overflow: hidden; }
  body {
    background: var(--stage);
    font-family: "Lato", Arial, sans-serif;
    position: relative;
  }
  .flyer {
    position: absolute;
    left: 324px; top: 10px;
    width: 552px; height: 780px;
    background: var(--paper);
    overflow: hidden;
    box-shadow: 0 2px 10px rgba(0,0,0,.12);
  }
  .flyer-shapes { position: absolute; inset: 0; }
  .brand {
    position: absolute; left: 26px; top: 32px;
    display: flex; align-items: center; gap: 10px;
    color: var(--pink); font-size: 30px; font-weight: 400; letter-spacing: .5px;
  }
  .brand-dot { width: 14px; height: 14px; border-radius: 50%; background: var(--pink); }
  .photo { position: absolute; }
  .photo--legs { left: 0; top: 104px; width: 172px; height: 150px; background: linear-gradient(135deg, var(--photo-cool), var(--photo-skin)); }
  .photo--client { left: 382px; top: 112px; width: 158px; height: 92px; border: 3px solid var(--white); background: linear-gradient(120deg, var(--photo-skin), #8d7a72); }
  .photo--led { left: 364px; top: 222px; width: 176px; height: 110px; border: 3px solid var(--teal); background: radial-gradient(circle at 60% 55%, #e37b6f, var(--photo-red) 45%, #5e4a55); }
  .block { position: absolute; color: var(--white); font-size: 10px; line-height: 1.32; font-weight: 400; }
  .block h2 { font-weight: 400; line-height: 1.05; margin-bottom: 3px; }
  .hair { left: 184px; top: 104px; width: 192px; }
  .hair h2 { font-size: 19px; }
  .cellulite { left: 20px; top: 266px; width: 338px; font-size: 9.5px; line-height: 1.3; }
  .cellulite h2 { font-size: 17px; }
  .pdt { left: 20px; top: 432px; width: 500px; }
  .pdt h2 { font-size: 18px; }
  .pdt .lead { font-size: 13px; margin-bottom: 2px; }
  .offer { position: absolute; left: 20px; top: 634px; color: var(--white); font-size: 21px; font-weight: 300; white-space: nowrap; }
  .resist { position: absolute; right: 20px; top: 690px; color: var(--pink); font-size: 22px; font-weight: 300; }
  .massage { position: absolute; right: 20px; top: 728px; text-align: right; color: var(--teal); font-size: 14px; line-height: 1.35; }
</style>
</head>
<body>
  <main class="flyer">
    <svg class="flyer-shapes" width="552" height="780" viewBox="0 0 552 780" aria-hidden="true">
      <polygon points="0,100 552,84 552,660 0,740" fill="var(--pink)"/>
      <polygon points="0,258 552,208 552,320 0,420" fill="var(--teal)"/>
      <polygon points="0,740 34,735 0,780" fill="var(--grey)"/>
      <g fill="var(--teal)">
        <polygon points="400,0 424,0 552,70 552,86"/>
        <polygon points="452,0 476,0 380,80 356,84"/>
        <polygon points="504,0 528,0 432,78 408,80"/>
        <polygon points="552,10 552,34 484,78 460,78"/>
      </g>
    </svg>

    <div class="brand"><span class="brand-dot"></span>Velvet Glow</div>

    <div class="photo photo--legs" role="img" aria-label="Photo of a laser hair removal treatment on a client's legs"></div>
    <div class="photo photo--client" role="img" aria-label="Photo of a woman receiving a body contouring treatment"></div>
    <div class="photo photo--led" role="img" aria-label="Photo of a client under red LED light therapy"></div>

    <section class="block hair">
      <h2>Laser Hair Removal</h2>
      <p>Non invasive and pain free<br>Look amazing and feel confident with a Hair Free body<br>Now is the time to start don't delay<br>1 treatment a month will ensure you are bikini hot for the summer months<br>Take full advantage of our OPENING SPECIALS of 30%-40% savings (Part payments available)</p>
    </section>

    <section class="block cellulite">
      <h2>CELLULITE &amp; FAT REDUCTION</h2>
      <p>Now you too can look amazing without invasive surgery, downtime or discomfort. Tara Wellbrook &amp; Monica Farrowdale are avid recipients of this treatment. Effective on all skin types and delivers fast measurable results for: Helping mums regain their pre-baby figures<br>Losing the love handles (but keeping the love)<br>Stretch mark reduction | Skin tightening | Cellulite busting on Arms, tummy, thighs<br>Man boob reduction | Latest technology: Bi Polar radio frequency (RF) infrared light<br>negative pressure (Vacuum)</p>
    </section>

    <section class="block pdt">
      <h2>PDT LED REJUVENATION<br>LIGHT THERAPY</h2>
      <p class="lead">ORVA Researchers found:</p>
      <p>Fibroblast and muscles grew 5 times faster, stimulates reconstruction of collagenous fibres<br>of the dermis. These findings and more assist with:<br>Remove freckles | sunburn pigmentation<br>Cures acne and hair follicle inflammation | Anti aging skin tightening<br>Reduces pore size | Improve the skin texture | Improves circulation<br>Red light : reduces pore size | softens skin wrinkles | reduces acne<br>Blue light: Kills the acne bacillus to eliminate acne, inhibit inflammation<br>Yellow light: Skin tightening, whitening and softens skin wrinkles<br>Purple light: combination of red &amp; blue lights treats acne scars<br>Orange light increases cell energy and accelerates metabolism</p>
    </section>

    <p class="offer">$55 Saving and relax under the lights.</p>
    <p class="resist">Who can resist???</p>
    <p class="massage">A soothing Hot stone massage therapy after:<br>A hard stressful day at work | Aches and muscular pain</p>
  </main>
</body>
</html>
```